Quill|Marlow & Petrie business card contest

We need a logo for an upscale boutique diversified company involved in real estate, investments, cattle, and more. Our businesses DO NOT need to be reflected in the business card nor do we want them noted. This is our logo and colors and we love our logo and colors. Our logo looks best against a black background and we like to include the firm name in our logo usage. importantly, the names Quill and Marlow are separated by | not / and we use an ampersand not the word and.
On the front of the card, we want to include:
company logo and name (Quill|Marlow & Petrie)
on the back, we would definitely include:
address, email, cell #
logo and name (smaller size than front)

The variable will be location of individual name and title (mine for example is ) - whether on the front OR on the back. interested in variations from which to choose
Dr. Owen T. Caldecott, CFA
Scientifique des Fusées Financières

we would like to use contemporary symbols for address, email address, cell # with an option for web site that we do not intend to use initially. we like two sided cards and believe this design should use four rounded corners with the standard size. we prefer thicker card stock and may look at metal.

```html
<!DOCTYPE html>
<html lang="en">
<head>
<meta charset="utf-8">
<title>Quill|Marlow &amp; Petrie — Business Card</title>
<link href="https://fonts.googleapis.com/css2?family=Lato:wght@400;700&display=swap" rel="stylesheet">
<style>
  :root {
    --bg: #2b2d31;
    --card-black: #0d0d0e;
    --card-white: #ffffff;
    --orange: #e0701f;
    --grey: #7a7a7a;
    --grey-dark: #4a4a4a;
    --text: #3a3a3a;
  }
  * { box-sizing: border-box; margin: 0; padding: 0; }
  html, body {
    width: 1200px; height: 900px; overflow: hidden;
    background: var(--bg);
    font-family: "Lato", sans-serif;
  }
  .canvas {
    width: 1200px; height: 900px;
    display: flex; flex-direction: column;
    align-items: center; justify-content: center; gap: 60px;
  }
  .card {
    width: 525px; height: 300px;
    border-radius: 28px;
    border: 5px solid var(--orange);
    position: relative; overflow: hidden;
  }
  .card--front {
    background: var(--card-black);
    display: flex; align-items: center; justify-content: center;
  }
  .brand {
    display: flex; align-items: center; gap: 14px;
    color: var(--grey); font-weight: 400;
  }
  .brand__square { width: 30px; height: 30px; background: var(--orange); flex: none; }
  .brand__name { font-size: 30px; letter-spacing: 0.5px; white-space: nowrap; }

  .card--back {
    background: var(--card-white);
    display: flex; align-items: center;
    padding: 0 30px 0 32px;
  }
  .card--back .brand { gap: 9px; color: var(--grey-dark); }
  .card--back .brand__square { width: 18px; height: 18px; }
  .card--back .brand__name { font-size: 17px; }
  .back__logo { width: 215px; display: flex; justify-content: center; }
  .divider {
    width: 2px; height: 150px; background: var(--orange);
    margin: 0 22px 0 14px; flex: none;
  }
  .contact { color: var(--text); }
  .contact__name {
    color: var(--orange); font-weight: 700; font-size: 19px; white-space: nowrap;
  }
  .contact__cred { font-size: 13px; color: var(--grey-dark); font-weight: 700; }
  .contact__title { font-size: 12px; font-weight: 700; color: var(--grey-dark); margin: 4px 0 14px; }
  .contact__list { list-style: none; font-size: 12.5px; font-weight: 700; color: var(--grey-dark); }
  .contact__list li { display: flex; align-items: flex-start; gap: 8px; margin-bottom: 6px; line-height: 1.35; }
  .icon { width: 14px; height: 14px; flex: none; margin-top: 1px; fill: var(--orange); }
</style>
</head>
<body>
<main class="canvas">
  <section class="card card--front" aria-label="Card front">
    <div class="brand">
      <span class="brand__square"></span>
      <span class="brand__name">Quill|Marlow &amp; Petrie</span>
    </div>
  </section>

  <section class="card card--back" aria-label="Card back">
    <div class="back__logo">
      <div class="brand">
        <span class="brand__square"></span>
        <span class="brand__name">Quill|Marlow &amp; Petrie</span>
      </div>
    </div>
    <div class="divider"></div>
    <div class="contact">
      <p class="contact__name">Dr. Owen T. Caldecott,<span class="contact__cred"> CFA</span></p>
      <p class="contact__title">Scientifique des Fusées Financières</p>
      <ul class="contact__list">
        <li>
          <svg class="icon" viewBox="0 0 24 24" aria-hidden="true"><path d="M6.6 10.8a15.1 15.1 0 0 0 6.6 6.6l2.2-2.2a1 1 0 0 1 1-.25 11.4 11.4 0 0 0 3.6.57 1 1 0 0 1 1 1V20a1 1 0 0 1-1 1A17 17 0 0 1 3 4a1 1 0 0 1 1-1h3.5a1 1 0 0 1 1 1c0 1.25.2 2.45.57 3.6a1 1 0 0 1-.25 1z"/></svg>
          <span>987 654 3210</span>
        </li>
        <li>
          <svg class="icon" viewBox="0 0 24 24" aria-hidden="true"><path d="M2 5h20v14H2z M2 5l10 8 10-8" fill="none" stroke="#e0701f" stroke-width="2.4"/><path d="M2 5h20l-10 8z"/></svg>
          <span>hello@quillmarlow.example</span>
        </li>
        <li>
          <svg class="icon" viewBox="0 0 24 24" aria-hidden="true"><path d="M12 2a7 7 0 0 0-7 7c0 5 7 13 7 13s7-8 7-13a7 7 0 0 0-7-7zm0 9.5A2.5 2.5 0 1 1 12 6.5a2.5 2.5 0 0 1 0 5z"/></svg>
          <span>4178 Harrow Lane<br>Suite 200, Brookfield, 48291</span>
        </li>
      </ul>
    </div>
  </section>
</main>
</body>
</html>
```